Specialised investor in e-mobility and energy wants business card design

We need a business card design that fits our existing corporate design. <The look and feel must be 'sharp'/'clean', dynamic, communicate momentum, professionalism etc (as one would imagine from a firm in the financial sector). We like the idea of a reverse-side of the card that includes the logo, and the name and contact details on the other. We expect the deliverable to be whatever format might be required to be able to get cards printed directly by a service such as marlo cards. Our website is www.obrel.finance

```html
<!DOCTYPE html>
<html lang="en">
<head>
<meta charset="utf-8">
<title>Obrel Finance – Business Card</title>
<link href="https://fonts.googleapis.com/css2?family=Roboto:wght@300;400;500;700&display=swap" rel="stylesheet">
<style>
  :root {
    --backdrop: #969696;
    --leaf: #82ad45;
    --forest: #243f15;
    --paper: #ffffff;
    --ink-soft: #5f5f5f;
    --rule: #c4c4c4;
  }
  * { margin: 0; padding: 0; box-sizing: border-box; }
  html, body {
    width: 1200px; height: 1000px; overflow: hidden;
    background: var(--backdrop);
    font-family: "Roboto", Arial, sans-serif;
  }
  .card {
    position: absolute; left: 293px; width: 615px; height: 351px;
  }
  .card-front {
    top: 100px;
    background: var(--leaf);
    display: flex; align-items: center; justify-content: center;
  }
  .front-pattern {
    position: absolute; inset: 0;
    background: linear-gradient(180deg, #86b04a 0%, #7fa943 100%);
  }
  .brand-lockup {
    position: relative;
    display: flex; align-items: center; gap: 16px;
    color: var(--forest);
    font-size: 52px; font-weight: 400; letter-spacing: 0.5px;
  }
  .brand-mark {
    width: 18px; height: 18px; border-radius: 50%;
    background: var(--forest);
  }
  .card-back { top: 511px; background: var(--paper); }
  .holder { position: absolute; top: 70px; width: 100%; text-align: center; }
  .holder-name { font-size: 23px; font-weight: 700; color: var(--forest); line-height: 30px; }
  .holder-role { font-size: 23px; font-weight: 300; color: var(--leaf); line-height: 28px; }
  .divider {
    position: absolute; top: 151px; left: 17px; width: 570px; height: 1px;
    background: linear-gradient(90deg, transparent 0%, var(--rule) 20%, var(--rule) 80%, transparent 100%);
  }
  .contacts {
    position: absolute; top: 180px; left: 20px; width: 580px; height: 72px;
    display: flex;
  }
  .contact {
    flex: 1; text-align: center; color: var(--ink-soft);
    font-size: 18px; font-weight: 400;
  }
  .contact + .contact { border-left: 1px solid var(--rule); }
  .contact svg { display: block; margin: 4px auto 8px; width: 18px; height: 18px; }
  .accent-line {
    position: absolute; top: 288px; left: 0; width: 100%; height: 3px; background: var(--leaf);
  }
  .footer-band {
    position: absolute; top: 295px; left: 0; width: 100%; height: 56px;
    background: var(--forest);
    display: flex; align-items: center; justify-content: center;
    color: var(--leaf); font-size: 17px; font-weight: 400;
  }
</style>
</head>
<body>
  <section class="card card-front">
    <div class="front-pattern" role="img" aria-label="Faint repeating brand name pattern in light green tones"></div>
    <div class="brand-lockup">
      <span class="brand-mark"></span>
      <span class="brand-name">Obrel Finance</span>
    </div>
  </section>

  <section class="card card-back">
    <div class="holder">
      <div class="holder-name">Daniel Haverly</div>
      <div class="holder-role">Partner</div>
    </div>
    <div class="divider"></div>
    <div class="contacts">
      <div class="contact">
        <svg viewBox="0 0 18 18" fill="none" stroke="#82ad45" stroke-width="1.2">
          <rect x="5" y="1" width="8" height="16" rx="1.5"/>
          <line x1="5" y1="13.5" x2="13" y2="13.5"/>
        </svg>
        +41 79555 0148
      </div>
      <div class="contact">
        <svg viewBox="0 0 18 18" fill="none" stroke="#82ad45" stroke-width="1.2">
          <rect x="1.5" y="4" width="15" height="11"/>
          <polyline points="1.5,4 9,10.5 16.5,4"/>
        </svg>
        daniel@obrel.finance
      </div>
      <div class="contact">
        <svg viewBox="0 0 18 18" fill="none" stroke="#82ad45" stroke-width="1.1">
          <circle cx="9" cy="9" r="7.5"/>
          <ellipse cx="9" cy="9" rx="3.5" ry="7.5"/>
          <line x1="1.5" y1="9" x2="16.5" y2="9"/>
          <line x1="2.5" y1="5.5" x2="15.5" y2="5.5"/>
          <line x1="2.5" y1="12.5" x2="15.5" y2="12.5"/>
        </svg>
        www.obrel.finance
      </div>
    </div>
    <div class="accent-line"></div>
    <div class="footer-band">Obrel Finance</div>
  </section>
</body>
</html>
```